Norvale Email Signature Banners – Fabrication Capability Series

www.Norvale.com.au is an Australian engineering and fabrication company specialising in fabrication and welding of :
steel piping spools,
skids and frames,
small volume process steel tanks
and general steel fabrication
We require four distinct banner designs for use in Teldrin Quillmark email signatures. Each banner will highlight a specific capability while maintaining a consistent brand identity.
Deliverables
Four banners total:
Piping Spools Fabrication – focus on precision welding and stainless steel pipework
Skid & Frames Fabrication – highlight skid systems and structural frames
Small Steel Tanks Fabrication – show fabricated tanks and workshop craftsmanship
General Fabrication Solutions – broad steel fabrication theme for company-wide use
Dimensions: 600–700 px wide × 100 px high
Format: PNG (preferred), small file size prefered
Resolution: 72 dpi
Background: non-transparent, industrial or workshop setting
Text examples:
1. Piping Spools Fabrication
Option A: “Expert Fabrication Solutions for Process Piping”
Option B: “Precision Welding for Complex Systems”
Option C: “Delivering Quality in Every Spool”
Option D: “Engineered for Flow, Built for Strength”
2. Skid & Frames Fabrication
Option A: “Custom Engineered Modular Systems”
Option B: “Built Strong. Designed Smart.”
Option C: “Reliable Frames for Industrial Performance”
Option D: “Modular Fabrication for Seamless Integration”
3. Small Steel Tanks Fabrication
Option A: “Precision Built for Your Needs”
Option B: “Compact Strength. Proven Durability.”
Option C: “Fabricated for Performance and Longevity”
Option D: “Small Tanks. Big Reliability.”
4. General Fabrication Solutions
Option A: “Quality Craftsmanship, Proven Results”
Option B: “Your Partner in Precision Fabrication”
Option C: “Engineering Excellence in Every Weld”
Option D: “Australian Fabrication. Global Standards.”
Style Direction
Clean, professional, and engineering‑focused
Use Norvale brand colours
Blend photo realism with vector clarity (no heavy gradients)
Include subtle industrial textures or workshop imagery
Typography: bold sans‑serif, legible at small scale
Usage Context
These banners will appear at the bottom of staff email signatures via Quillmark Email Signature Tool for Teldrin 365, so clarity and fast loading are essential. No Logo is required in the banners.
Reference
Existing Norvale signature is attached. Colour palette to match the signature style and logo.
Target Market(s)
Engineering and construction companies,
Industry/Entity Type
Engineering fabrication design

```html
<!DOCTYPE html>
<html lang="en">
<head>
<meta charset="utf-8">
<title>Norvale Email Signature Banners – Fabrication Capability Series</title>
<link href="https://fonts.googleapis.com/css2?family=Poppins:ital,wght@0,700;1,600&display=swap" rel="stylesheet">
<style>
  :root {
    --page-bg: #ededed;
    --panel-dark: #11151e;
    --brand-blue: #29a8e0;
    --brand-blue-deep: #0b5f8f;
    --photo-light: #1f9ad6;
    --photo-shadow: #063a5a;
    --text-white: #ffffff;
  }
  * { margin: 0; padding: 0; box-sizing: border-box; }
  html, body {
    width: 1200px;
    height: 876px;
    overflow: hidden;
    background: var(--page-bg);
  }
  .banner-set {
    position: relative;
    width: 1200px;
    height: 876px;
  }
  .banner {
    position: absolute;
    left: 113px;
    width: 974px;
    height: 162px;
    overflow: hidden;
    background: var(--panel-dark);
  }
  .banner--skids { top: 82px; }
  .banner--tanks { top: 265px; }
  .banner--general { top: 448px; }
  .banner--piping { top: 633px; }

  .banner__photo {
    position: absolute;
    top: 0;
    right: 0;
    width: 620px;
    height: 100%;
  }
  .banner--skids .banner__photo {
    background: linear-gradient(200deg, var(--photo-light) 0%, #1479b3 45%, var(--photo-shadow) 100%);
  }
  .banner--tanks .banner__photo {
    background: linear-gradient(110deg, var(--photo-shadow) 0%, #1a8cc8 45%, #0d4f78 100%);
  }
  .banner--general .banner__photo {
    background: linear-gradient(170deg, #2ba7e2 0%, #136fa6 50%, var(--photo-shadow) 100%);
  }
  .banner--piping .banner__photo {
    background: radial-gradient(ellipse at 62% 85%, #8fd8ff 0%, #1c8fcf 25%, #0a4a72 60%, #05273f 100%);
  }
  .banner__frame {
    position: absolute;
    inset: 0;
    width: 100%;
    height: 100%;
  }
  .banner__headline {
    position: absolute;
    left: 44px;
    top: 50%;
    transform: translateY(-50%);
    font-family: "Poppins", sans-serif;
    font-weight: 700;
    font-size: 25px;
    line-height: 33px;
    color: var(--text-white);
    letter-spacing: 0.1px;
  }
  .banner__line { display: block; white-space: nowrap; }
  .accent {
    position: relative;
    color: var(--brand-blue);
    font-style: italic;
    font-weight: 600;
  }
  .accent::after {
    content: "";
    position: absolute;
    left: -8px;
    right: 4px;
    bottom: -3px;
    height: 1px;
    background: var(--brand-blue);
  }
</style>
</head>
<body>
<main class="banner-set">

  <section class="banner banner--skids">
    <div class="banner__photo" role="img" aria-label="Steel structural frame of a modular skid under construction against the sky, in blue tones"></div>
    <svg class="banner__frame" viewBox="0 0 974 162" preserveAspectRatio="none" aria-hidden="true">
      <path d="M0 0 H443 Q432 108 375 162 H0 Z" fill="var(--panel-dark)"/>
      <path d="M443 0 Q432 108 375 162" fill="none" stroke="var(--brand-blue)" stroke-width="3.5"/>
    </svg>
    <h2 class="banner__headline">
      <span class="banner__line">Custom <span class="accent">Engineered</span></span>
      <span class="banner__line">Modular Systems</span>
    </h2>
  </section>

  <section class="banner banner--tanks">
    <div class="banner__photo" role="img" aria-label="Gloved hands measuring steel sections with a caliper in a workshop, in blue tones"></div>
    <svg class="banner__frame" viewBox="0 0 974 162" preserveAspectRatio="none" aria-hidden="true">
      <path d="M0 0 H443 Q432 108 375 162 H0 Z" fill="var(--panel-dark)"/>
      <path d="M443 0 Q432 108 375 162" fill="none" stroke="var(--brand-blue)" stroke-width="3.5"/>
    </svg>
    <h2 class="banner__headline">
      <span class="banner__line">Compact Strength</span>
      <span class="banner__line">Proven <span class="accent">Durability</span></span>
    </h2>
  </section>

  <section class="banner banner--general">
    <div class="banner__photo" role="img" aria-label="Stacks of steel pipes inside a large fabrication workshop, in blue tones"></div>
    <svg class="banner__frame" viewBox="0 0 974 162" preserveAspectRatio="none" aria-hidden="true">
      <path d="M0 0 H443 Q432 108 375 162 H0 Z" fill="var(--panel-dark)"/>
      <path d="M443 0 Q432 108 375 162" fill="none" stroke="var(--brand-blue)" stroke-width="3.5"/>
    </svg>
    <h2 class="banner__headline">
      <span class="banner__line">Engineering <span class="accent">Excellence</span></span>
      <span class="banner__line">in Every Weld</span>
    </h2>
  </section>

  <section class="banner banner--piping">
    <div class="banner__photo" role="img" aria-label="Welder at work with bright sparks flying, in blue tones"></div>
    <svg class="banner__frame" viewBox="0 0 974 162" preserveAspectRatio="none" aria-hidden="true">
      <path d="M0 0 H443 Q432 108 375 162 H0 Z" fill="var(--panel-dark)"/>
      <path d="M443 0 Q432 108 375 162" fill="none" stroke="var(--brand-blue)" stroke-width="3.5"/>
    </svg>
    <h2 class="banner__headline">
      <span class="banner__line">Expert <span class="accent">Fabrication Solutions</span></span>
      <span class="banner__line">for Process Piping</span>
    </h2>
  </section>

</main>
</body>
</html>
```